Web Design Project

We need to have you design a 7 page design for ecommerce site.

The design will consist of a Home Page, Category Landing Page, Category Product Page, Product Page, Cart Page, Gift Registry Page, and Virtual Place Setting Page

The goal will be a design which is similar to:

http://www.pellorin.example/ in terms of layout of the home page

http://www.pellorin.example/decor The category landing pages will look a bit like this

http://www.pellorin.example/decor/decorative-pillows. The category product pages will look like this , however, will have more of a layered navigation on the left where you can sort by brand, price, finish, etc. instead of ability to shop by category here

http://www.pellorin.example/p/velmora-dinnerware The product page can be similar to this one

Please add a product to cart as the cart page can be very similar to the look and feel here.

For the gift registry landing page, here are some examples: http://www.hollowcrestgoods.example/regHome.asp

http://www.ferrant-dalby.example/registry/

Last, we need to create a virtual place setting app like this: http://www.luminacasa.example/style-your-table

But more better and stylish, mapping in with the theme.

Industry/Entity Type

Shop

Requirements
Must have
• - This needs to have a sophisticated, luxurious look and feel. Please make sure to design a 'showcase' style page for the main categorly landing pages.

```html
<!DOCTYPE html>
<html lang="en">
<head>
<meta charset="utf-8">
<title>Settle &amp; Sup — Style your table</title>
<link href="https://fonts.googleapis.com/css2?family=Mulish:wght@400;600;700&display=swap" rel="stylesheet">
<style>
:root{
  --dark:#454545;
  --green:#b5c98e;
  --green-text:#9fba6e;
  --ink:#222;
  --muted:#6b6b6b;
  --rule:#c9c9c9;
  --pale:#ebebeb;
  --white:#fff;
  --porcelain-edge:#d6d6d6;
  --silver-light:#eeeeee;
  --silver-dark:#a9a9a9;
}
*{box-sizing:border-box;margin:0;padding:0}
html,body{width:987px;height:1200px;overflow:hidden;background:var(--white)}
body{font-family:"Mulish",sans-serif;color:var(--ink)}
.page{position:absolute;left:0;top:0;width:1024px;height:1245px;transform:scale(.9639);transform-origin:0 0}
.abs{position:absolute}
a{color:inherit;text-decoration:none}

.masthead{left:72px;top:35px;width:879px;height:167px;background:var(--dark);padding:14px}
.masthead-inner{position:relative;width:100%;height:100%;border:2px solid var(--white)}
.brand{left:24px;top:14px;width:106px;height:108px;background:var(--white);display:flex;align-items:center;justify-content:center;text-align:center;color:var(--green-text);font-weight:700;font-size:17px;line-height:1.15}
.account{right:12px;top:14px;display:flex;align-items:center;gap:14px;color:var(--white);font-size:14px}
.account .ico{display:inline-block;vertical-align:middle;margin-right:6px}
.btn-green{background:var(--green);color:var(--white);border:1px solid #d8e3c3;padding:3px 6px;font-size:14px}
.search{right:12px;top:80px;display:flex;height:30px}
.search input{width:170px;border:1px solid #ddd;padding:0 8px;font:11px "Mulish",sans-serif;color:#999}
.search button{width:72px;background:var(--green);color:var(--white);border:1px solid #d8e3c3;font:14px "Mulish",sans-serif}

.nav{left:72px;top:210px;width:879px;height:47px}
.nav a{position:absolute;top:0;width:120px;height:47px;background:var(--dark);color:var(--white);display:flex;align-items:center;justify-content:center;font-size:16px;border:1px solid #333}
.nav a.current{background:var(--green);border-color:#cfdcb5}

.title{left:78px;top:278px;font-size:31px;color:var(--green-text);font-weight:400}

.sidebar{left:70px;top:324px;width:216px;height:622px;border:1px solid var(--rule);padding:8px 12px}
.cat{font-size:16px;padding:14px 0 5px 28px;border-bottom:1px solid var(--rule);position:relative;margin-top:6px}
.cat::before{content:"";position:absolute;left:5px;top:19px;border-left:8px solid var(--ink);border-top:5px solid transparent;border-bottom:5px solid transparent}
.cat.open::before{border-left:5px solid transparent;border-right:5px solid transparent;border-top:8px solid var(--green);border-bottom:0;left:4px;top:20px}
.sub{list-style:none;padding:14px 0 4px 30px;font-size:15px}
.sub li{height:33px}

.carousel{left:286px;top:434px;width:108px;height:310px;background:#c8c8c8;padding:24px 6px}
.carousel .arrow{position:absolute;left:46px;width:14px;height:10px}
.thumb{height:81px;margin-bottom:6px;background:var(--white);border:1px solid #aaa;display:flex;justify-content:center;align-items:center}
.thumb div{width:26px;height:62px;border-radius:13px 13px 4px 4px;background:linear-gradient(#f6f6f6 0%,#e4e4e4 45%,#8b8b8b 100%)}

.piece{position:absolute}
.plate{border-radius:50%;background:radial-gradient(circle at 50% 50%,#fdfdfd 0%,#f7f7f7 55%,#ececec 75%,var(--porcelain-edge) 100%);box-shadow:0 1px 4px rgba(0,0,0,.12)}
.salad{left:438px;top:319px;width:170px;height:170px}
.dinner{left:510px;top:500px;width:298px;height:295px}
.goblet{left:822px;top:300px;width:82px;height:195px;border-radius:10px 10px 30px 30px;background:linear-gradient(#f4f4f4 0%,#e3e3e3 55%,#f2f2f2 72%,#d9d9d9 100%)}
.flat-left{left:440px;top:555px;width:55px;height:205px;border-radius:14px;background:linear-gradient(90deg,var(--silver-light),var(--silver-dark) 50%,var(--silver-light))}
.flat-right{left:832px;top:530px;width:95px;height:230px;border-radius:18px;background:linear-gradient(90deg,var(--silver-light),var(--silver-dark) 50%,var(--silver-light))}

.actions a{position:absolute;top:821px;width:175px;height:48px;background:var(--dark);color:var(--white);display:flex;align-items:center;justify-content:center;font-size:19px}
.note{left:392px;top:889px;width:556px;height:58px;background:var(--pale);display:flex;align-items:center;justify-content:center;font-size:15px;color:var(--muted)}

.foot-col{top:985px;width:180px;height:180px;background:var(--dark);padding:18px 10px;color:var(--white);font-size:13px;line-height:1.35}
.foot-col h3{color:var(--green);font-size:15px;margin-bottom:4px}
.social{display:flex;gap:5px;margin-top:12px}
.social span{width:33px;height:33px;background:var(--green);border:1px solid #d8e3c3;border-radius:3px;display:block}
.subscribe{left:671px;top:985px;width:279px;height:180px;background:var(--dark);padding:9px}
.subscribe-inner{position:relative;border:2px solid var(--white);height:100%;padding:8px 9px;color:var(--white);font-size:13px;line-height:1.35}
.subscribe h3{color:var(--green);font-size:15px;margin-bottom:4px}
.subscribe form{position:absolute;left:9px;bottom:18px;display:flex;height:30px}
.subscribe input{width:162px;border:1px solid #ddd;padding:0 7px;font:10px "Mulish",sans-serif;color:#aaa}
.subscribe button{width:72px;background:var(--green);color:var(--white);border:1px solid #d8e3c3;font:11px "Mulish",sans-serif}

.legal{left:0;top:1182px;width:1024px;text-align:center;font-size:12px;color:#666;line-height:1.45;font-weight:600}
.legal .dot{display:inline-block;width:12px;height:12px;border-radius:50%;background:#38a8e0;vertical-align:-2px;margin:0 10px}
</style>
</head>
<body>
<div class="page">
  <header class="masthead abs">
    <div class="masthead-inner">
      <div class="brand abs">Settle<br>&amp; Sup</div>
      <div class="account abs">
        <a href="#"><svg class="ico" width="14" height="18" viewBox="0 0 14 18"><circle cx="7" cy="5" r="4.5" fill="#b5c98e"/><path d="M0 18v-4a5 5 0 0 1 5-5h4a5 5 0 0 1 5 5v4z" fill="#b5c98e"/></svg>Sign in / Join</a>
        <a href="#"><svg class="ico" width="30" height="20" viewBox="0 0 30 20"><path d="M1 3h5l4 12h14l3-9" stroke="#b5c98e" stroke-width="2.5" fill="none"/><circle cx="12" cy="18" r="1.8" fill="#b5c98e"/><circle cx="22" cy="18" r="1.8" fill="#b5c98e"/><text x="15" y="8" fill="#fff" font-size="10" font-family="Mulish">0</text></svg>Cart</a>
        <a class="btn-green" href="#">Checkout</a>
      </div>
      <form class="search abs"><input value="Enter keyword or item" aria-label="Search"><button type="button">Search</button></form>
    </div>
  </header>

  <nav class="nav abs">
    <a href="#" style="left:0">Home</a>
    <a href="#" style="left:127px">Flatware</a>
    <a class="current" href="#" style="left:253px">Dinnerware</a>
    <a href="#" style="left:379px">Drinkware</a>
    <a href="#" style="left:506px">Barware</a>
    <a href="#" style="left:634px">Linens</a>
    <a href="#" style="left:758px">Table accents</a>
  </nav>

  <h1 class="title abs">Style your table</h1>

  <aside class="sidebar abs">
    <div class="cat">FLATWARE</div>
    <div class="cat">DINNERWARE</div>
    <div class="cat open">DRINKWARE</div>
    <ul class="sub">
      <li>Orin Vale</li><li>Corvo</li><li>Glasshaus</li><li>Marenna</li><li>Tavoli</li><li>Halden Stemware</li><li>Castello Stemware</li>
    </ul>
    <div class="cat">BARWARE</div>
    <div class="cat">LINENS</div>
    <div class="cat" style="border-bottom:0">TABLE ACCENTS</div>
  </aside>

  <div class="carousel abs">
    <svg class="arrow" style="top:5px" viewBox="0 0 14 10"><path d="M1 9l6-7 6 7" stroke="#fff" stroke-width="2.5" fill="none"/></svg>
    <div class="thumb"><div role="img" aria-label="Wine glass"></div></div>
    <div class="thumb"><div role="img" aria-label="Wine glass"></div></div>
    <div class="thumb"><div role="img" aria-label="Wine glass"></div></div>
    <svg class="arrow" style="bottom:6px" viewBox="0 0 14 10"><path d="M1 1l6 7 6-7" stroke="#fff" stroke-width="2.5" fill="none"/></svg>
  </div>

  <section class="setting" aria-label="Place setting">
    <div class="piece plate salad" role="img" aria-label="White scalloped salad plate"></div>
    <div class="piece goblet" role="img" aria-label="Crystal goblet"></div>
    <div class="piece flat-left" role="img" aria-label="Silver dinner and salad forks"></div>
    <div class="piece plate dinner" role="img" aria-label="White scalloped dinner plate"></div>
    <div class="piece flat-right" role="img" aria-label="Silver knife, soup spoon and teaspoon"></div>
  </section>

  <div class="actions">
    <a href="#" style="left:391px">UNDO</a>
    <a href="#" style="left:585px">ADD TO CART</a>
    <a href="#" style="left:775px">CLEAR ALL</a>
  </div>
  <p class="note abs">*Images may not be to scale. Click on each piece for more detail.</p>

  <footer>
    <div class="foot-col abs" style="left:72px">
      <h3>GENERAL</h3>About Us<br>Customer Service<br>Returns &amp; Exchanges<br>Privacy Policy<br>Terms &amp; Conditions<br>Contact Us
    </div>
    <div class="foot-col abs" style="left:272px;padding-left:13px">
      <h3>ONLINE SHOPPING</h3>Virtual Placesetting<br>Gift registry<br>Business gifts<br>Wish Lists<br>Affiliates
    </div>
    <div class="foot-col abs" style="left:472px;padding-left:14px">
      <h3>OUR COMMUNITY</h3>Store Events<br>Design Trade<br>Catalog Requests<br>Follow us
      <div class="social"><span></span><span></span><span></span><span></span></div>
    </div>
    <div class="subscribe abs">
      <div class="subscribe-inner">
        <h3>Subscribe</h3>Join our email list to learn about new products and special offers.
        <form><input value="enter email address" aria-label="Email"><button type="button">Subscribe</button></form>
      </div>
    </div>
    <p class="legal abs">For questions or assistance<span class="dot"></span>1-800-555-0142<br>Copyright © Settle &amp; Sup 2012</p>
  </footer>
</div>
</body>
</html>
```